CareWillow Brand Standards and Core Values

I would like to have frameable posters made up for each office using our brand standards. I would like the posters to include:Our Vision Statement:We are transforming the healthcare staffing and homecare industry with our people-oriented, world-class team. Clients choose us, and develop lasting bonds with our team because of our impeccably high standards and our reputation for always remembering this is, first and foremost, a people business. We consistently go the extra mile to ensure our nurses and those being cared for are at all times, treated with dignity and respect. We hold ourselves and those we work with to the highest possible standards. We consistently deliver what we promise, and whenever possible, even more. Our Mission Statement:We go above and beyond to ensure our clients receive the right care and the right people at the right time. Our rigorous recruitment standards result in strong caregivers who are trusted for their expertise, experience and compassion. Our Values:Through our genuine caring and compassion, we are committed to honor all with whom we interact. We are grounded in our faith and dedicated to working together as a family that consistently and passionately lives our values. Compassion Integrity and honesty Faith Decisive action Constant and never-ending improvement Personal ownership Excellence Positive attitude Passion RespectWho we are:We are friendly, servant leaders who have a sense of urgency to meet the needs of our nurses and clients. We prioritize personal relationships with genuine caring and compassion. We inspire others through our passion and energy.Our main colors are: HEX# 5C80DE, HEX# BDE080, HEX# 8C8C8Caccent colors are: HEX# 95D6E3, HEX# AD59AB, HEX# 002E57

Target Market(s)

office employee inspiration

Font styles to use
Other font styles liked:
• Verdana

Colors

Designer to choose colors to be used in the design.

Requirements
Must have
• the core values listed in description
Nice to have
• colors given in description, something fun and inspiring for office employees to help motivate them !
Should not have
• colors that are not company colors. I have listed HEX codes in description

```html
<!DOCTYPE html>
<html lang="en">
<head>
<meta charset="utf-8">
<title>CareWillow – Vision, Mission, Values</title>
<link href="https://fonts.googleapis.com/css2?family=Arimo:wght@400;700&display=swap" rel="stylesheet">
<style>
  :root {
    --page-bg: #e6e6e6;
    --blue: #5c80de;
    --navy: #002e57;
    --purple: #ad59ab;
    --grey: #8c8c8c;
    --pink: #f1b9ca;
    --pink-soft: #f8dbe4;
    --paper: #f6f4f5;
    --gold: #e0b84a;
  }
  html, body {
    margin: 0;
    width: 1200px;
    height: 900px;
    overflow: hidden;
    background: var(--page-bg);
    font-family: "Arimo", Arial, sans-serif;
  }
  .poster {
    position: absolute;
    left: 272px;
    top: 10px;
    width: 656px;
    height: 880px;
    overflow: hidden;
    background: var(--paper);
  }
  .poster-backdrop {
    position: absolute;
    inset: 0;
    background:
      linear-gradient(180deg, var(--pink) 0%, var(--pink-soft) 22%, var(--paper) 40%, var(--paper) 75%, var(--pink-soft) 86%, var(--pink) 100%);
  }
  .heading {
    position: absolute;
    margin: 0;
    font-weight: 400;
    color: var(--blue);
    line-height: 1;
    white-space: nowrap;
  }
  .heading--vision { left: 122px; top: 96px; font-size: 78px; letter-spacing: -1.5px; }
  .heading--mission { left: 124px; top: 330px; font-size: 82px; letter-spacing: -2px; }
  .statement {
    position: absolute;
    margin: 0;
    color: var(--navy);
    font-size: 12.8px;
    line-height: 16.2px;
  }
  .statement--vision { left: 132px; top: 178px; width: 432px; }
  .statement--mission { left: 129px; top: 412px; width: 474px; }
  .vision-icon { position: absolute; left: 22px; top: 104px; }
  .mission-target {
    position: absolute;
    left: 470px;
    top: 322px;
    width: 76px;
    height: 76px;
    border-radius: 50%;
    background: radial-gradient(circle, #95d6e3 0 18%, #c9553f 19% 42%, var(--gold) 43% 100%);
  }
  .values-tab {
    position: absolute;
    left: 368px;
    top: 470px;
    width: 238px;
    height: 68px;
    border: 2px solid var(--purple);
    border-radius: 4px 4px 0 0;
    border-bottom: none;
    background: var(--paper);
    display: flex;
    align-items: center;
    justify-content: flex-end;
    padding-right: 14px;
    box-sizing: border-box;
  }
  .heading--values { position: static; font-size: 52px; letter-spacing: -0.5px; }
  .values-box {
    position: absolute;
    left: 18px;
    top: 538px;
    width: 610px;
    height: 210px;
    border: 2px solid var(--purple);
    border-radius: 4px;
    box-sizing: border-box;
    padding: 12px 30px 0 16px;
    background: rgba(246, 244, 245, 0.85);
  }
  .values-list { list-style: none; margin: 0; padding: 0; }
  .values-item {
    display: flex;
    gap: 10px;
    color: var(--navy);
    font-size: 12.8px;
    line-height: 16.4px;
    margin-bottom: 15px;
  }
  .values-item svg { flex: none; margin-top: 1px; }
  .brand-plate {
    position: absolute;
    left: 247px;
    top: 750px;
    width: 150px;
    height: 130px;
    background: #f7f7f7;
    display: flex;
    flex-direction: column;
    align-items: center;
    justify-content: center;
    gap: 14px;
  }
  .brand-dot { width: 26px; height: 26px; border-radius: 50%; background: var(--blue); }
  .brand-name { color: var(--grey); font-size: 20px; font-weight: 400; }
</style>
</head>
<body>
  <main class="poster">
    <div class="poster-backdrop" role="img" aria-label="Soft pink faceted geometric background"></div>

    <svg class="vision-icon" width="92" height="54" viewBox="0 0 92 54" aria-hidden="true">
      <path d="M2 27 C22 2 70 2 90 27 C70 52 22 52 2 27 Z" fill="var(--navy)"/>
      <circle cx="46" cy="27" r="16" fill="#fff"/>
      <circle cx="46" cy="27" r="10" fill="var(--navy)"/>
    </svg>
    <h1 class="heading heading--vision">VISION</h1>
    <p class="statement statement--vision">We are transforming the healthcare staffing and homecare industry with our people-oriented, world-class team. Clients choose us, and develop lasting bonds with our team because of our impeccably high standards and our reputation for always remembering this is, first and foremost, a people business. We consistently go the extra mile to ensure our nurses and those being cared for are at all times, treated with dignity and respect. We hold ourselves and those we work with to the highest possible standards. We consistently deliver what we promise, and whenever possible, even more.</p>

    <h2 class="heading heading--mission">MISSION</h2>
    <div class="mission-target" role="img" aria-label="Target with an arrow in the bullseye"></div>
    <p class="statement statement--mission">We go above and beyond to ensure our clients receive the right care and the right people at the right time. Our rigorous recruitment standards result in strong caregivers who are trusted for their expertise, experience and compassion.</p>

    <div class="values-tab"><h2 class="heading heading--values">VALUES</h2></div>
    <section class="values-box">
      <ul class="values-list">
        <li class="values-item">
          <svg width="18" height="16" viewBox="0 0 18 16" aria-hidden="true"><rect x="1" y="4" width="11" height="11" fill="none" stroke="var(--navy)" stroke-width="1.5"/><path d="M3 9 L6.5 13 L17 1" fill="none" stroke="var(--navy)" stroke-width="2.5"/></svg>
          <span>Through our genuine caring and compassion, we are committed to honor all with whom we interact. We are grounded in our faith and dedicated to working together as a family that consistently and passionately lives our values.</span>
        </li>
        <li class="values-item">
          <svg width="18" height="16" viewBox="0 0 18 16" aria-hidden="true"><rect x="1" y="4" width="11" height="11" fill="none" stroke="var(--navy)" stroke-width="1.5"/><path d="M3 9 L6.5 13 L17 1" fill="none" stroke="var(--navy)" stroke-width="2.5"/></svg>
          <span>Compassion Integrity and honesty Faith Decisive action Constant and never-ending improvement Personal ownership Excellence Positive attitude Passion RespectWho we are: We are friendly, servant leaders who have a sense of urgency to meet the needs of our nurses and clients.</span>
        </li>
        <li class="values-item">
          <svg width="18" height="16" viewBox="0 0 18 16" aria-hidden="true"><rect x="1" y="4" width="11" height="11" fill="none" stroke="var(--navy)" stroke-width="1.5"/><path d="M3 9 L6.5 13 L17 1" fill="none" stroke="var(--navy)" stroke-width="2.5"/></svg>
          <span>We prioritize personal relationships with genuine caring and compassion. We inspire others through our passion and energy</span>
        </li>
      </ul>
    </section>

    <footer class="brand-plate">
      <span class="brand-dot" aria-hidden="true"></span>
      <span class="brand-name">CareWillow</span>
    </footer>
  </main>
</body>
</html>
```